HTML Email template look and feel

Hi, we have been sending out various emails to our clients and they have been a mix of anything from plain text to some html emails that were done for us, i am looking to get a nice design and layout for our HTML emails to keep them looking professional and consistent. What I am looking for is an html email template that has a nice edgy but professional look and feel. Ie header and table styling i suppose. Most of the data we send is either in a 2 or 4 column table layout as such.
Table A
Firm A 6
Firm B 124
Firm C 32435
Table B
Firm A 6 Firm D 4546
Firm B 124 Firm E 3545
Firm C 32435 Firm F 44
For some background our website is http://www.quellmarkets.example/
and our logo is on there, and i have attached one of the html emails we are currently sending.
Reason: Just wanted to see what comes in over the weekend before we decide

```html
<!DOCTYPE html>
<html lang="en">
<head>
<meta charset="utf-8">
<title>Quell Markets – Daily Execution Summary</title>
<link rel="stylesheet" href="https://fonts.googleapis.com/css2?family=Roboto:wght@400;500;700&display=swap">
<style>
  :root {
    --page-bg: #ffffff;
    --ink: #1d1d1d;
    --ink-soft: #2b2b2b;
    --link: #1a8fd6;
    --bar-top: #2ea3e0;
    --bar-bottom: #0a6fb6;
    --banner-light: #eef5fc;
    --banner-mid: #7fb8ec;
    --banner-deep: #1a5fc4;
    --rule: #dcdcdc;
    --head-top: #ffffff;
    --head-bottom: #ececec;
  }
  * { box-sizing: border-box; margin: 0; padding: 0; }
  html, body {
    width: 1050px; height: 1200px; overflow: hidden;
    background: var(--page-bg);
    font-family: "Roboto", Arial, sans-serif;
    color: var(--ink);
  }
  .preheader {
    position: absolute; top: 24px; left: 0; width: 1050px;
    text-align: center; font-size: 16px; color: var(--ink-soft);
  }
  .preheader a { color: var(--link); text-decoration: none; }

  .email { position: absolute; left: 73px; top: 73px; width: 914px; }

  .banner {
    position: relative; height: 209px;
    background:
      radial-gradient(ellipse at 78% 95%, #ffffff 0%, rgba(255,255,255,0) 35%),
      linear-gradient(100deg, var(--banner-light) 0%, var(--banner-light) 30%, var(--banner-mid) 55%, var(--banner-deep) 75%, var(--banner-mid) 90%, var(--banner-light) 100%);
  }
  .brand {
    position: absolute; left: 30px; top: 78px;
    display: flex; align-items: center; gap: 16px;
    font-size: 46px; font-weight: 700; color: #111111; letter-spacing: 1px;
  }
  .brand-square { width: 34px; height: 34px; background: #1a8fd6; }

  .summary-bar {
    height: 44px; display: flex; justify-content: space-between; align-items: center;
    padding: 0 14px;
    background: linear-gradient(var(--bar-top), var(--bar-bottom));
    color: #ffffff; font-weight: 700; font-size: 19px;
  }

  .report {
    margin-top: 8px; height: 812px - 333px;
    height: 479px;
    border: 1px solid var(--rule);
    padding: 0 17px;
    height: 812px;
  }
  .section-title {
    font-size: 24px; font-weight: 500; color: var(--ink-soft);
    padding-left: 12px;
  }
  .report .section-title:first-child { margin-top: 22px; }

  .volume-table {
    width: 878px; margin-top: 22px;
    border-collapse: collapse; table-layout: fixed;
  }
  .volume-table th, .volume-table td {
    border: 1px solid var(--rule); text-align: center;
  }
  .volume-table th {
    height: 66px; font-size: 19px; font-weight: 500; line-height: 1.2;
    background: linear-gradient(var(--head-top), var(--head-bottom));
  }
  .volume-table td { height: 45px; font-size: 19px; }
  .volume-table .symbol { font-weight: 500; }

  .sector-heading { margin-top: 38px; }
  .sector-grid { margin-top: 18px; width: 878px; }
  .sector-row { display: flex; border: 1px solid var(--rule); margin-bottom: 12px; }
  .sector { flex: 1; }
  .sector + .sector { border-left: 1px solid var(--rule); }
  .sector-name {
    height: 45px; line-height: 45px; text-align: center;
    font-size: 19px; font-weight: 500;
    background: linear-gradient(var(--head-top), var(--head-bottom));
  }
  .tickers {
    height: 47px; display: flex; justify-content: space-around; align-items: center;
    font-size: 19px; border-top: 1px solid #f0f0f0;
  }
</style>
</head>
<body>
  <p class="preheader">If this html does not render correctly, <a href="http://www.quellmarkets.example/">click here</a> for online version</p>

  <div class="email">
    <header class="banner" role="img" aria-label="Abstract blue light-streak banner artwork">
      <div class="brand"><span>QUELL MARKETS</span><span class="brand-square"></span></div>
    </header>

    <div class="summary-bar">
      <span>27,490,544 Shares Executed</span>
      <span>12/01/2011</span>
    </div>

    <main class="report">
      <h2 class="section-title">Top 10 Symbols As of % of volume</h2>
      <table class="volume-table">
        <thead>
          <tr><th>Symbol</th><th>% of previous<br>day’s volume</th><th>Symbol</th><th>% of previous<br>day’s volume</th></tr>
        </thead>
        <tbody>
          <tr><td class="symbol">WIRT</td><td>23.84%</td><td class="symbol">WIRT</td><td>23.84%</td></tr>
          <tr><td class="symbol">LHNB</td><td>16.71%</td><td class="symbol">LHNB</td><td>16.71%</td></tr>
          <tr><td class="symbol">LAVQ</td><td>14.61%</td><td class="symbol">LAVQ</td><td>14.61%</td></tr>
          <tr><td class="symbol">EXRN</td><td>12.34%</td><td class="symbol">EXRN</td><td>12.34%</td></tr>
          <tr><td class="symbol">PKRD</td><td>14.06%</td><td class="symbol">PKRD</td><td>14.06%</td></tr>
        </tbody>
      </table>

      <h2 class="section-title sector-heading">Top 5 by sector</h2>
      <div class="sector-grid">
        <div class="sector-row">
          <div class="sector"><div class="sector-name">Consumer Discretionary</div><div class="tickers"><span>KDT</span><span>SELO</span><span>YRB</span><span>BXQ</span><span>MVRA</span></div></div>
          <div class="sector"><div class="sector-name">Consumer Discretionary</div><div class="tickers"><span>KDT</span><span>SELO</span><span>YRB</span><span>BXQ</span><span>MVRA</span></div></div>
        </div>
        <div class="sector-row">
          <div class="sector"><div class="sector-name">Consumer Staples</div><div class="tickers"><span>KDT</span><span>SELO</span><span>YRB</span><span>BXQ</span><span>MVRA</span></div></div>
          <div class="sector"><div class="sector-name">Information Technology</div><div class="tickers"><span>KDT</span><span>SELO</span><span>YRB</span><span>BXQ</span><span>MVRA</span></div></div>
        </div>
        <div class="sector-row">
          <div class="sector"><div class="sector-name">Consumer Staples</div><div class="tickers"><span>KDT</span><span>SELO</span><span>YRB</span><span>BXQ</span><span>MVRA</span></div></div>
          <div class="sector"><div class="sector-name">Information Technology</div><div class="tickers"><span>KDT</span><span>SELO</span><span>YRB</span><span>BXQ</span><span>MVRA</span></div></div>
        </div>
      </div>
    </main>
  </div>
</body>
</html>
```